Criação de Papelaria (6 itens) para Arquitetura
" Sou recém formada em Design de Interiores e pretendo começar a divulgar meu negócio. Já fiz alguns trabalhos / projetos, mas ainda não consegui alavancar minha marca. Meu foco será a realização de projetos residenciais, comerciais e empresariais. As atividades vão desde a entrevista inicial para entendimento das necessidades do cliente, passando pela preparação dos projetos com imagens renderizadas, plantas baixas, projetos de marcenaria, iluminação, gesso etc., incluindo também acompanhamento a lojas para escolha de materiais / móveis até o acompanhamento da obra e fiscalização dos trabalhos executados por terceiros. "

```html
<!DOCTYPE html>
<html lang="pt-BR">
<head>
<meta charset="utf-8">
<title>Lia Moreno · Papelaria</title>
<link href="https://fonts.googleapis.com/css2?family=Montserrat:wght@300;400;500&display=swap" rel="stylesheet">
<style>
  :root {
    --bg: #e9e8ea;
    --paper: #ffffff;
    --rose: #d9a092;
    --rose-light: #ecc8bf;
    --charcoal: #4b4753;
    --charcoal-dark: #3f3b46;
    --ink: #6f6c74;
    --rule: #d9d9dc;
  }
  * { box-sizing: border-box; margin: 0; padding: 0; }
  html, body { width: 1200px; height: 1200px; overflow: hidden; }
  body {
    background: var(--bg);
    font-family: "Montserrat", sans-serif;
    color: var(--ink);
    position: relative;
  }
  .sheet {
    position: absolute;
    background: var(--paper);
    box-shadow: 0 2px 8px rgba(0,0,0,.12);
  }

  /* Notepad */
  .notepad { left: 468px; top: 72px; width: 264px; height: 516px; }
  .brand { display: flex; flex-direction: column; align-items: center; }
  .brand-mark { width: 14px; height: 14px; border: 1.5px solid var(--rose); margin-bottom: 6px; }
  .brand-name { font-weight: 300; color: var(--rose); letter-spacing: .14em; white-space: nowrap; }
  .brand-tag { font-weight: 400; color: var(--ink); letter-spacing: .28em; white-space: nowrap; text-transform: uppercase; }
  .notepad .brand { margin-top: 16px; }
  .notepad .brand-name { font-size: 15px; }
  .notepad .brand-tag { font-size: 4.5px; margin-top: 3px; }
  .notepad-divider { position: absolute; left: 14px; right: 14px; top: 76px; height: 1px; background: var(--rose-light); }
  .notepad-date { position: absolute; right: 26px; top: 84px; font-size: 9px; letter-spacing: 10px; color: var(--ink); border-bottom: 1px solid var(--rule); padding: 0 0 1px 12px; }
  .notepad-lines {
    position: absolute; left: 14px; right: 14px; top: 112px; height: 336px;
    background: repeating-linear-gradient(to bottom, transparent 0 23px, var(--rule) 23px 24px);
  }
  .notepad-footer {
    position: absolute; left: 14px; right: 14px; top: 464px;
    display: flex; justify-content: space-between; font-size: 4.5px; line-height: 1.5;
  }
  .contact { display: flex; align-items: center; gap: 4px; }
  .contact svg { width: 8px; height: 8px; flex: none; }
  .notepad-band { position: absolute; left: 0; right: 0; bottom: 10px; height: 4px; background: var(--rose); }

  /* Folder */
  .folder-back {
    left: 269px; top: 612px; width: 360px; height: 504px;
    background: linear-gradient(180deg, var(--charcoal) 0%, var(--charcoal-dark) 100%);
  }
  .folder-back .contact-list { position: absolute; left: 20px; bottom: 62px; font-size: 6px; color: #d7d4da; display: flex; flex-direction: column; gap: 9px; }
  .folder-back .contact svg { width: 10px; height: 10px; }
  .folder-back .brand { position: absolute; left: 0; right: 0; bottom: 36px; }
  .folder-back .brand-mark { width: 10px; height: 10px; margin-bottom: 3px; }
  .folder-back .brand-name { font-size: 9px; color: var(--rose); }
  .folder-back .brand-tag { font-size: 3px; color: #cfcbd3; margin-top: 2px; }
  .folder-back-band { position: absolute; left: 150px; right: 0; bottom: 22px; height: 4px; background: var(--rose); }

  .folder-front { left: 636px; top: 612px; width: 336px; height: 504px; }
  .folder-front .brand { position: absolute; left: 0; right: 0; top: 190px; }
  .folder-front .brand-mark { width: 30px; height: 30px; border-width: 2.5px; margin-bottom: 12px; }
  .folder-front .brand-name { font-size: 32px; color: var(--ink); letter-spacing: .1em; }
  .folder-front .brand-tag { font-size: 8px; color: var(--rose); margin-top: 6px; letter-spacing: .3em; }
  .folder-front-band { position: absolute; left: 14px; right: 14px; bottom: 22px; height: 4px; background: var(--rose); }
</style>
</head>
<body>
  <svg width="0" height="0" style="position:absolute">
    <defs>
      <symbol id="icon-phone" viewBox="0 0 10 10"><circle cx="5" cy="5" r="5" fill="currentColor"/><path d="M3.3 2.6l1 1-.5.7c.3.7.8 1.2 1.5 1.5l.7-.5 1 1-.7.9C4.8 7 3 5.2 2.8 3.3z" fill="#fff"/></symbol>
      <symbol id="icon-pin" viewBox="0 0 10 10"><circle cx="5" cy="5" r="5" fill="currentColor"/><path d="M5 2.2a1.9 1.9 0 0 1 1.9 1.9C6.9 5.5 5 7.8 5 7.8S3.1 5.5 3.1 4.1A1.9 1.9 0 0 1 5 2.2z" fill="#fff"/><circle cx="5" cy="4.1" r=".7" fill="currentColor"/></symbol>
      <symbol id="icon-web" viewBox="0 0 10 10"><circle cx="5" cy="5" r="5" fill="currentColor"/><circle cx="5" cy="5" r="2.6" fill="none" stroke="#fff" stroke-width=".6"/><path d="M2.4 5h5.2M5 2.4c-1.2 1.4-1.2 3.8 0 5.2M5 2.4c1.2 1.4 1.2 3.8 0 5.2" fill="none" stroke="#fff" stroke-width=".5"/></symbol>
    </defs>
  </svg>

  <section class="sheet notepad">
    <div class="brand">
      <span class="brand-mark"></span>
      <span class="brand-name">LIA MORENO</span>
      <span class="brand-tag">Design de Interiores</span>
    </div>
    <div class="notepad-divider"></div>
    <div class="notepad-date">//</div>
    <div class="notepad-lines"></div>
    <div class="notepad-footer">
      <div class="contact" style="color:var(--charcoal)"><svg><use href="#icon-pin"/></svg><span>Rua das Acácias, 120</span></div>
      <div class="contact" style="color:var(--charcoal)"><svg><use href="#icon-phone"/></svg><span>(11) 4000-1234</span></div>
      <div class="contact" style="color:var(--charcoal)"><svg><use href="#icon-web"/></svg><span>liamoreno.com<br>oi@liamoreno.com</span></div>
    </div>
    <div class="notepad-band"></div>
  </section>

  <section class="sheet folder-back">
    <div class="contact-list">
      <div class="contact" style="color:#ffffff"><svg style="color:var(--rose)"><use href="#icon-phone"/></svg><span>(11) 4000-1234</span></div>
      <div class="contact"><svg style="color:var(--rose)"><use href="#icon-web"/></svg><span>liamoreno.com</span></div>
      <div class="contact"><svg style="color:var(--rose)"><use href="#icon-pin"/></svg><span>Rua das Acácias, 120</span></div>
    </div>
    <div class="brand">
      <span class="brand-mark"></span>
      <span class="brand-name">LIA MORENO</span>
      <span class="brand-tag">Design de Interiores</span>
    </div>
    <div class="folder-back-band"></div>
  </section>

  <section class="sheet folder-front">
    <div class="brand">
      <span class="brand-mark"></span>
      <span class="brand-name">LIA MORENO</span>
      <span class="brand-tag">Design de Interiores</span>
    </div>
    <div class="folder-front-band"></div>
  </section>
</body>
</html>
```